Company document Header needed

Using our current logo, I need a Designer to create a header for use on our company documents. This header will include our business address, phone, fax, website address

Reason: Dear designers, I am so pleased with the many different options that have been presented, that I wish to purchase several of them from a few different designers. I will get with the pixel forum folks and figure out what is the best way to do this. In the meantime, I am extending the deadline to allow for a few edits such as our phone number and such. thanks to you all for your excellent work. RT

Designers,

Please take a look and edit any of your submissions that have incorrect info on them:  the correct info is below:

Business name is: Brass Kite, Inc.

website address is:  www.brasskite-example.com

Office #:  (855) BrassKite  

Fax#:  (858) 516-2947  (generally I do not intend to need this on any materials unless it balances a look)

email:  info@brasskite-example.com

Address:  782 Larkwood Blvd. suite 2310  San Diego, CA  92174

Thanks!

```html
<!DOCTYPE html>
<html lang="en">
<head>
<meta charset="utf-8">
<title>Brass Kite, Inc. — Letterhead</title>
<link rel="stylesheet" href="https://fonts.googleapis.com/css2?family=PT+Sans+Narrow:wght@400;700&display=swap">
<style>
  :root {
    --backdrop: #3a3a3a;
    --paper: #ffffff;
    --brand-blue: #0a5a94;
    --brand-navy: #123a66;
    --ink-grey: #6b6b6b;
    --accent-faint: #e9f4fd;
  }
  html, body {
    margin: 0;
    padding: 0;
    width: 1200px;
    height: 907px;
    overflow: hidden;
    background: var(--backdrop);
  }
  .sheet {
    position: absolute;
    left: 294px;
    top: 23px;
    width: 611px;
    height: 861px;
    background: var(--paper);
    overflow: hidden;
  }
  .sheet__decor {
    position: absolute;
    left: 312px;
    top: 0;
    width: 261px;
    height: 861px;
    background: linear-gradient(180deg, var(--accent-faint), rgba(233, 244, 253, 0.55));
  }
  .brand {
    position: absolute;
    left: 0;
    top: 57px;
    width: 170px;
    height: 56px;
    display: flex;
    align-items: center;
    gap: 9px;
    padding-left: 12px;
    box-sizing: border-box;
  }
  .brand__mark {
    width: 26px;
    height: 26px;
    background: var(--brand-blue);
    flex: none;
  }
  .brand__name {
    font-family: "PT Sans Narrow", sans-serif;
    font-weight: 700;
    font-size: 24px;
    color: var(--brand-blue);
    letter-spacing: 0.5px;
    white-space: nowrap;
  }
  .contact {
    position: absolute;
    left: 183px;
    top: 98px;
    font-family: "PT Sans Narrow", sans-serif;
    font-size: 9.5px;
    line-height: 10.5px;
    color: var(--ink-grey);
  }
  .contact p { margin: 0; }
  .contact__company,
  .contact__web {
    font-weight: 700;
    color: var(--brand-navy);
  }
  .contact__web { margin-top: 8px !important; }
</style>
</head>
<body>
  <main class="sheet">
    <div class="sheet__decor" role="img" aria-label="Faint brand decoration band"></div>
    <div class="brand">
      <span class="brand__mark"></span>
      <span class="brand__name">Brass Kite</span>
    </div>
    <address class="contact" style="font-style: normal;">
      <p class="contact__company">Brass Kite, Inc.</p>
      <p>782 Larkwood Blvd. suite 2310 San Diego,</p>
      <p>CA 92174; Office: (855) BrassKite</p>
      <p>Fax: (858) 516-2947</p>
      <p>email: info@brasskite-example.com</p>
      <p class="contact__web">www.brasskite-example.com</p>
    </address>
  </main>
</body>
</html>
```